Business Card + Letterhead Design for BELMARSH IMPORTS INC.

We already have a logo; now we need a business card + letterhead. We import and distribute flags and souvenirs with an emphasis on soccer related memorabilia. We target various ethnic markets and sporting goods stores. "Wandering Keepsakes"

```html
<!DOCTYPE html>
<html lang="en">
<head>
<meta charset="utf-8">
<title>Belmarsh Imports Inc. — Letterhead and Business Cards</title>
<link href="https://fonts.googleapis.com/css2?family=Arimo:wght@400;700&family=Open+Sans:wght@400;600;700&display=swap" rel="stylesheet">
<style>
  :root {
    --maroon: #8b2a2d;
    --ink: #1c1c1c;
    --grey-arc: #9d9d9e;
    --text-grey: #555555;
    --paper: #ffffff;
    --backdrop: #ececec;
    --card-dark: #0e0e0e;
    --card-mid: #4a4a4a;
  }
  * { box-sizing: border-box; margin: 0; padding: 0; }
  html, body { width: 1156px; height: 1200px; overflow: hidden; }
  body {
    background: var(--backdrop);
    font-family: "Arimo", Arial, sans-serif;
    color: var(--ink);
    position: relative;
  }

  /* Letterhead */
  .letterhead {
    position: absolute; left: 42px; top: 42px;
    width: 767px; height: 1075px;
    background: var(--paper);
    overflow: hidden;
  }
  .letterhead .arc { position: absolute; display: block; }
  .letterhead .arc-top { left: 0; top: 0; }
  .letterhead .arc-bottom { right: 0; bottom: 0; }

  .brand {
    position: absolute; display: flex; align-items: center; gap: 12px;
    font-family: "Open Sans", Arial, sans-serif; font-weight: 700;
    color: var(--maroon); line-height: 1;
  }
  .brand .dot { border-radius: 50%; background: var(--ink); flex: none; }
  .brand .name { display: flex; flex-direction: column; gap: 5px; }

  .letterhead .brand { right: 52px; top: 74px; }
  .letterhead .brand .dot { width: 40px; height: 40px; }
  .letterhead .brand .line1 { font-size: 34px; letter-spacing: 1px; }
  .letterhead .brand .line2 { font-size: 15px; letter-spacing: 9px; }

  .contact-band {
    position: absolute; left: 0; top: 128px; width: 100%; height: 44px;
    background: var(--maroon); color: #fff;
    font-family: "Open Sans", Arial, sans-serif; font-size: 10px; line-height: 16px;
  }
  .contact-band .col { position: absolute; top: 6px; }
  .contact-band .col-phone { left: 82px; }
  .contact-band .col-web { left: 317px; }
  .contact-band .col-address { left: 550px; display: flex; gap: 8px; }
  .contact-band .row { display: flex; align-items: center; gap: 5px; }
  .icon { width: 9px; height: 9px; flex: none; }

  .letter-body {
    position: absolute; left: 71px; top: 355px; width: 629px;
    font-size: 13px; line-height: 21.8px; color: var(--ink);
  }
  .letter-body .salutation {
    font-size: 21px; color: var(--text-grey); margin-bottom: 5px; line-height: 26px;
  }
  .letter-body p.para { text-align: justify; margin-bottom: 22px; }
  .letter-body .closing { margin-top: 0; }
  .signature {
    display: block; width: 160px; height: 58px; margin-top: 34px;
    background: linear-gradient(90deg, #e9e9e9, #f4f4f4);
  }
  .signatory { margin-top: 34px; font-size: 15px; line-height: 18px; color: var(--text-grey); }

  /* Business cards */
  .card {
    position: absolute; left: 777px; width: 338px; height: 201px; overflow: hidden;
  }
  .card-front { top: 338px; background: var(--paper); }
  .card-back {
    top: 580px;
    background: radial-gradient(ellipse at 35% 40%, var(--card-mid) 0%, #232323 55%, var(--card-dark) 100%);
  }
  .card .arc { position: absolute; right: 0; display: block; }
  .card-front .arc { top: 0; }
  .card-back .arc { bottom: 0; }

  .card-front .holder {
    position: absolute; right: 113px; top: 22px; text-align: right;
    font-family: "Open Sans", Arial, sans-serif; color: #444; font-size: 7.5px; line-height: 11px;
  }
  .holder .person { font-weight: 700; font-size: 10.5px; color: #333; line-height: 13px; }
  .holder .company { margin-bottom: 10px; }
  .holder .row { display: flex; justify-content: flex-end; align-items: center; gap: 3px; }
  .holder .gap { height: 9px; }
  .holder .icon { width: 7px; height: 7px; }

  .card-front .brand { left: 14px; top: 132px; gap: 9px; }
  .card .brand .dot { width: 28px; height: 28px; }
  .card .brand .line1 { font-size: 24px; }
  .card .brand .line2 { font-size: 11px; letter-spacing: 6px; }
  .card-front .brand .line2 { color: var(--ink); }

  .card-back .brand { left: 64px; top: 54px; color: #ffffff; }
  .card-back .brand .dot { background: #ffffff; }
  .card-back .site {
    position: absolute; left: 101px; top: 102px;
    font-family: "Open Sans", Arial, sans-serif; font-size: 9px; letter-spacing: 3px; color: #cfcfcf;
  }
</style>
</head>
<body>

<section class="letterhead" aria-label="Letterhead">
  <svg class="arc arc-top" width="330" height="330" viewBox="0 0 330 330" aria-hidden="true">
    <path d="M322 0 A322 322 0 0 1 0 322 L0 225 A225 225 0 0 0 225 0 Z" fill="var(--grey-arc)"/>
  </svg>
  <svg class="arc arc-bottom" width="200" height="200" viewBox="0 0 200 200" aria-hidden="true">
    <path d="M200 5 A195 195 0 0 0 5 200 L72 200 A128 128 0 0 1 200 72 Z" fill="var(--grey-arc)"/>
  </svg>

  <div class="brand">
    <span class="dot"></span>
    <span class="name"><span class="line1">BELMARSH</span><span class="line2">IMPORTS</span></span>
  </div>

  <div class="contact-band">
    <div class="col col-phone">
      <div class="row"><svg class="icon" viewBox="0 0 10 10"><path d="M2 1 L4 1 L4.6 3 L3.4 3.8 Q4.6 6 6.2 6.6 L7 5.4 L9 6 L9 8 Q5 9 2.2 6 Q1 3.6 2 1Z" fill="#fff"/></svg>(647) 555-0192</div>
      <div class="row"><svg class="icon" viewBox="0 0 10 10"><rect x="1" y="2" width="8" height="6" rx="1" fill="#fff"/></svg>(866) 555-0147</div>
    </div>
    <div class="col col-web">
      <div class="row"><svg class="icon" viewBox="0 0 10 10"><rect x="1" y="2" width="8" height="6" fill="none" stroke="#fff"/><path d="M1 2 L5 5.5 L9 2" fill="none" stroke="#fff"/></svg>sales@belmarshimports.ca</div>
      <div class="row"><svg class="icon" viewBox="0 0 10 10"><path d="M3 1 L3 8 L5 6.5 L6.5 9 L7.5 8.5 L6 6 L8 5.5 Z" fill="#fff"/></svg>belmarshimports.ca</div>
    </div>
    <div class="col col-address">
      <svg class="icon" viewBox="0 0 10 10" style="margin-top:4px"><rect x="1" y="3" width="8" height="5" fill="#fff"/><rect x="3" y="1" width="4" height="2" fill="#fff"/></svg>
      <div>2207-18 Harrow Lane,<br>Toronto, ON, Canada M4K 2B7</div>
    </div>
  </div>

  <div class="letter-body">
    <p class="salutation">Dear client</p>
    <p class="para">We have obtained your name and address from Website, and we are writing to enquire whether you would be willing to establish business relations with us. We have been importers of shoes for many years. At present, We are interested in extending our, range and would appreciate your catalogues and quotations. If your prices are competitive we would expect to transact a significant volume of business. We look forward to your early reply.</p>
    <p class="para">We have obtained your name and address from Website, and we are writing to enquire whether you would be willing to establish business relations with us. We have been importers of shoes for many years. At present, We are interested in extending our, range and would appreciate your catalogues and quotations. If your prices are competitive we would expect to transact a significant volume of business. We look forward to your early reply.</p>
    <p class="para">We have obtained your name and address from Website, and we are writing to enquire whether you would be willing to establish business relations with us. We have been importers of shoes for many years. At present, We are interested in extending our, range and would appreciate your catalogues and quotations. If your prices are competitive we would expect to transact a significant volume of business. We look forward to your early reply.</p>
    <p class="closing">Yours Sincerely,</p>
    <span class="signature" role="img" aria-label="Handwritten signature of Mira Tolland"></span>
    <p class="signatory">Mira Tolland<br>Creative Director</p>
  </div>
</section>

<section class="card card-front" aria-label="Business card, front">
  <svg class="arc" width="110" height="110" viewBox="0 0 110 110" aria-hidden="true">
    <path d="M0 100 A100 100 0 0 1 100 0 L110 0 L110 42 L100 42 A58 58 0 0 0 42 100 Z" fill="var(--ink)"/>
  </svg>
  <div class="holder">
    <div class="person">DANIEL CORVELL</div>
    <div class="company">BELMARSH IMPORTS INC.</div>
    <div class="row">(647) 555-0192 <svg class="icon" viewBox="0 0 10 10"><path d="M2 1 L4 1 L4.6 3 L3.4 3.8 Q4.6 6 6.2 6.6 L7 5.4 L9 6 L9 8 Q5 9 2.2 6 Q1 3.6 2 1Z" fill="none" stroke="#777"/></svg></div>
    <div class="row">(866) 555-0147 <svg class="icon" viewBox="0 0 10 10"><rect x="1" y="2" width="8" height="6" rx="1" fill="none" stroke="#777"/></svg></div>
    <div class="gap"></div>
    <div class="row">Email: sales@belmarshimports.ca <svg class="icon" viewBox="0 0 10 10"><rect x="1" y="2" width="8" height="6" fill="none" stroke="#777"/><path d="M1 2 L5 5.5 L9 2" fill="none" stroke="#777"/></svg></div>
    <div class="row">Web: belmarshimports.ca <svg class="icon" viewBox="0 0 10 10"><path d="M3 1 L3 8 L5 6.5 L6.5 9 L7.5 8.5 L6 6 L8 5.5 Z" fill="none" stroke="#777"/></svg></div>
  </div>
  <div class="brand">
    <span class="dot"></span>
    <span class="name"><span class="line1">BELMARSH</span><span class="line2">IMPORTS</span></span>
  </div>
</section>

<section class="card card-back" aria-label="Business card, back">
  <svg class="arc" width="110" height="110" viewBox="0 0 110 110" aria-hidden="true">
    <path d="M6 110 A104 104 0 0 1 110 6 L110 46 A64 64 0 0 0 46 110 Z" fill="var(--grey-arc)"/>
  </svg>
  <div class="brand">
    <span class="dot"></span>
    <span class="name"><span class="line1">BELMARSH</span><span class="line2">IMPORTS</span></span>
  </div>
  <p class="site">belmarshimports.ca</p>
</section>

</body>
</html>
```